Website, SMS, Chat Translator business

Im very open to the design, idea and card Shape. I just have my Web and business Names. Needs to be in Vector and PDF format Please. Based out of Larkmoor, NV . Giving list of names to see what is the best naming and resonates with the brand. brivolent-nexa.com
brivolent-kits.com
quellmarkforportals.com everyitemquellmark.com. txt-quellmark.com . brivolentingkits.com quellmarkforportal.com.
talkquellmarks.com

```html
<!DOCTYPE html>
<html lang="en">
<head>
<meta charset="utf-8">
<title>Brivolent Nexa — Business Card</title>
<link rel="stylesheet" href="https://fonts.googleapis.com/css2?family=Open+Sans:wght@400;600&family=Playfair+Display:wght@400&display=swap">
<style>
  :root {
    --page-bg: #e2e2e2;
    --teal-light: #4bb6c8;
    --teal-deep: #0096c0;
    --teal-panel: #008ab4;
    --teal-corner: #4aafc0;
    --ink-teal: #1a86a8;
    --label-bg: #4bb3c3;
    --white: #ffffff;
    --palm-green: #2fae4a;
    --palm-trunk: #a0743c;
  }
  * { margin: 0; padding: 0; box-sizing: border-box; }
  html, body {
    width: 1200px; height: 1200px; overflow: hidden;
    background: var(--page-bg);
    font-family: "Open Sans", Arial, sans-serif;
  }
  .card {
    position: absolute; left: 145px; width: 907px; height: 516px;
    overflow: hidden;
  }
  .card--front { top: 71px; }
  .card--back { top: 611px; background: var(--white); }
  .card-bg { position: absolute; inset: 0; width: 100%; height: 100%; }

  .brand-name {
    position: absolute; color: var(--white);
    font-family: "Open Sans", Arial, sans-serif; font-weight: 400;
    white-space: nowrap; transform: translate(-50%, -50%);
  }
  .card--front .brand-name { left: 453px; top: 217px; font-size: 52px; }
  .card--back .brand-name { left: 180px; top: 277px; font-size: 34px; }

  .tagline {
    position: absolute; left: 260px; width: 387px; top: 309px; height: 61px;
    border-top: 1px solid rgba(255,255,255,0.45);
    border-bottom: 1px solid rgba(255,255,255,0.45);
  }
  .tagline-text {
    position: absolute; left: 50%; top: 50%; transform: translate(-50%, -50%);
    white-space: nowrap; color: var(--white);
    font-family: "Playfair Display", Georgia, serif; font-size: 33px;
    letter-spacing: 1.5px;
  }

  .holder { position: absolute; left: 397px; top: 100px; }
  .holder-name { color: var(--ink-teal); font-size: 34px; font-weight: 400; line-height: 1.1; }
  .holder-role {
    display: inline-block; margin-top: 4px; padding: 0 4px;
    background: var(--label-bg); color: var(--white); font-size: 22px; line-height: 28px;
  }

  .contacts { position: absolute; left: 415px; top: 240px; list-style: none; }
  .contact {
    display: flex; align-items: center; height: 36px; margin-bottom: 12px;
    color: var(--ink-teal); font-size: 22px; white-space: nowrap;
  }
  .contact:nth-child(3) { margin-bottom: 9px; }
  .contact-icon { width: 32px; height: 32px; margin-right: 9px; flex: none; }

  .palm-art {
    position: absolute; left: 776px; top: 395px; width: 126px; height: 121px;
    background: linear-gradient(160deg, var(--palm-green) 0%, var(--palm-green) 45%, var(--palm-trunk) 100%);
    opacity: 0.85; border-radius: 40px 40px 0 0;
  }
</style>
</head>
<body>
  <section class="card card--front">
    <svg class="card-bg" viewBox="0 0 907 516" preserveAspectRatio="none" aria-hidden="true">
      <rect width="907" height="516" fill="var(--teal-deep)"/>
      <polygon points="0,0 683,0 199,516 0,516" fill="var(--teal-light)"/>
    </svg>
    <div class="brand-name">brivolent nexa</div>
    <div class="tagline"><span class="tagline-text">WEB TRANSLATION&nbsp; SERVICES</span></div>
  </section>

  <section class="card card--back">
    <svg class="card-bg" viewBox="0 0 907 516" preserveAspectRatio="none" aria-hidden="true">
      <rect width="358" height="516" fill="var(--teal-panel)"/>
      <polygon points="0,0 239,0 0,251" fill="var(--teal-corner)"/>
    </svg>
    <div class="brand-name">brivolent nexa</div>

    <div class="holder">
      <h1 class="holder-name">YOUR NAME</h1>
      <span class="holder-role">Administrator</span>
    </div>

    <ul class="contacts">
      <li class="contact">
        <svg class="contact-icon" viewBox="0 0 24 24" aria-hidden="true"><path fill="var(--ink-teal)" d="M6.6 10.8a15 15 0 0 0 6.6 6.6l2.2-2.2c.3-.3.7-.4 1-.2 1.1.4 2.3.6 3.6.6.6 0 1 .4 1 1V20c0 .6-.4 1-1 1A17 17 0 0 1 3 4c0-.6.4-1 1-1h3.5c.6 0 1 .4 1 1 0 1.3.2 2.5.6 3.6.1.3 0 .7-.2 1z"/></svg>
        305-555-0142
      </li>
      <li class="contact">
        <svg class="contact-icon" viewBox="0 0 24 24" aria-hidden="true"><path fill="var(--ink-teal)" d="M12 2a7 7 0 0 0-7 7c0 5.2 7 13 7 13s7-7.8 7-13a7 7 0 0 0-7-7zm0 9.5A2.5 2.5 0 1 1 12 6.5a2.5 2.5 0 0 1 0 5z"/></svg>
        Larkmoor, NV
      </li>
      <li class="contact">
        <svg class="contact-icon" viewBox="0 0 24 24" aria-hidden="true"><rect x="3" y="6" width="18" height="12" fill="var(--ink-teal)"/><path d="M3 6l9 7 9-7" fill="none" stroke="#fff" stroke-width="1.3"/></svg>
        contact@brivolent-nexa.com
      </li>
      <li class="contact">
        <svg class="contact-icon" viewBox="0 0 24 24" aria-hidden="true"><g fill="none" stroke="var(--ink-teal)" stroke-width="1.2"><circle cx="12" cy="12" r="9"/><ellipse cx="12" cy="12" rx="4" ry="9"/><path d="M3 12h18M4.5 7.5h15M4.5 16.5h15"/></g></svg>
        www.brivolent-nexa.com
      </li>
    </ul>

    <div class="palm-art" role="img" aria-label="Illustration of two palm trees"></div>
  </section>
</body>
</html>
```